Flyer-Design für Lindenblüten Abend Kurs Vol. 2
Zielgruppe
Seminare, Vorträge , Therapien, Beratung, Coaching
WEchseljahre Beratung
Sexualtherapie, Sexualberatung
Mentaltraining
Es soll Frauen gefallen und ermuntern zum Seminar zu kommen, frü Thema Wechseljahre interessieren
Aufgabenstellung
Grösse A5 Hochkant

```html
<!DOCTYPE html>
<html lang="de">
<head>
<meta charset="utf-8">
<title>Lindenblüten Abend Kurs Vol. 2 – Flyer</title>
<link href="https://fonts.googleapis.com/css2?family=Oswald:wght@300;500&family=Fira+Sans:ital,wght@0,400;0,600;1,400&family=Bitter:wght@700&family=Alfa+Slab+One&display=swap" rel="stylesheet">
<style>
:root{
  --blue:#00a9d0;
  --blue-soft:#52bcd8;
  --green:#c5c93f;
  --yellow:#fff15a;
  --ink:#1d1d1b;
  --muted:#444444;
  --white:#ffffff;
  --page:#ffffff;
}
*{margin:0;padding:0;box-sizing:border-box}
html,body{width:877px;height:1200px;overflow:hidden;background:var(--page)}
.flyer{position:relative;width:877px;height:1200px;background:var(--white);overflow:hidden;font-family:"Fira Sans",sans-serif;color:var(--ink)}
.photo-edge{position:absolute;left:0;top:0;width:20px;height:598px;background:linear-gradient(180deg,#b9c98a,#8a9a5a 60%,#b8a57a)}
.green-edge{position:absolute;left:0;top:598px;width:20px;height:338px;background:var(--green)}
.photo-woman{position:absolute;left:504px;top:0;width:373px;height:936px;background:linear-gradient(180deg,#dfe9c6 0%,#a9bfd8 30%,#8f9fc7 50%,#b9cd7a 68%,var(--green) 82%)}
.content{position:absolute;left:20px;top:0;width:484px;height:936px;background:var(--white)}

.rule{position:absolute;left:79px;width:370px;height:9px;background:var(--yellow)}
.rule.top{top:54px}
.rule.bottom{top:266px}
.date{position:absolute;left:75px;top:62px;font-family:"Oswald",sans-serif;font-weight:500;color:var(--blue);font-size:108px;line-height:1;letter-spacing:-1px;white-space:nowrap}
.date .year{font-size:60px;letter-spacing:0}
.label{position:absolute;left:0;width:527px;top:176px;text-align:center;font-family:"Oswald",sans-serif;font-weight:300;color:var(--blue);font-size:80px;line-height:1}

.headline{position:absolute;left:42px;top:294px;font-weight:600;color:var(--blue);font-size:30px;line-height:34px;letter-spacing:-.4px;white-space:nowrap}
.intro{position:absolute;left:41px;top:413px;width:452px;column-count:2;column-gap:18px;font-size:10.2px;line-height:16.2px;text-align:justify;hyphens:auto;-webkit-hyphens:auto}

.section-title{position:absolute;left:42px;font-weight:600;color:var(--blue);font-size:31px;line-height:36px;letter-spacing:.1px;white-space:nowrap}
.title-learn{top:568px}
.title-know{top:720px}

.points{position:absolute;list-style:none;font-weight:600;font-size:11.6px;line-height:16px}
.points li{position:relative;padding-left:15px;margin-bottom:5px}
.points li::before{content:"";position:absolute;left:0;top:3px;width:8px;height:8px;background:var(--blue)}
.learn-a{left:44px;top:612px;width:230px}
.learn-b{left:282px;top:612px;width:215px}
.know{left:44px;top:758px;width:392px}

.info-circle{position:absolute;left:494px;top:548px;width:354px;height:352px;border-radius:50%;background:var(--blue);border:6px solid var(--white);color:var(--white);text-align:center;font-family:"Oswald",sans-serif;font-weight:500}
.time{position:absolute;left:0;right:0;top:80px;font-size:18px;line-height:42px;white-space:nowrap}
.time b{color:var(--yellow);font-size:40px;font-weight:500}
.place{position:absolute;left:0;right:0;top:123px;font-size:24px;line-height:33px;white-space:nowrap}
.place .thin{font-weight:300}
.price{position:absolute;left:0;right:0;top:190px;font-family:"Fira Sans",sans-serif;font-weight:600;color:var(--yellow);font-size:28px;line-height:66px;white-space:nowrap}
.price b{font-size:66px;font-weight:600}
.price sup{font-size:26px;line-height:0;vertical-align:30px}
.note{position:absolute;left:0;right:0;top:262px;font-family:"Fira Sans",sans-serif;font-style:italic;font-weight:400;color:var(--ink);font-size:11px;line-height:18px;white-space:nowrap}

.brand-circle{position:absolute;left:524px;top:450px;width:163px;height:154px;border-radius:50%;background:var(--blue-soft);border:5px solid var(--white);display:flex;align-items:center;justify-content:center;font-family:"Fira Sans",sans-serif;font-weight:600;color:var(--white);font-size:17px}

.band{position:absolute;left:0;top:936px;width:877px;height:143px;background:var(--blue)}
.band p{position:absolute;left:330px;top:28px;width:463px;font-family:"Bitter",serif;font-weight:700;color:var(--white);font-size:14.6px;line-height:22.4px;text-align:justify}
.portrait{position:absolute;left:85px;top:930px;width:213px;height:192px;border-radius:50%;border:5px solid var(--white);background:radial-gradient(circle at 50% 45%,#d9c2b0,#a89a92 55%,#cfd7e3)}

.signup{position:absolute;left:0;right:0;top:1093px;text-align:center}
.signup h3{font-family:"Alfa Slab One",serif;font-weight:400;color:var(--blue);font-size:20px;line-height:24px}
.signup p{font-size:13px;line-height:20px;color:var(--muted)}
.signup .accent{color:var(--blue);font-weight:600}
</style>
</head>
<body>
<main class="flyer">
  <div class="photo-edge" role="img" aria-label="Unscharfer Baumhintergrund im Grünen"></div>
  <div class="green-edge"></div>
  <div class="photo-woman" role="img" aria-label="Foto: Frau in blauer Strickjacke und Jeans sitzt lächelnd im Gras"></div>

  <section class="content"></section>
  <div class="rule top"></div>
  <div class="date">23.04.<span class="year">2017.</span></div>
  <div class="label">SEMINAR</div>
  <div class="rule bottom"></div>

  <p class="headline">Ein Neuwerden, ein Loslassen,<br>ein einzigartiges Geschenk<br>und Herausforderung zugleich!</p>

  <p class="intro">Viele Frauen befinden, dass mit dem Klimakterium eine Last von ihren Schultern fällt. Endlich dürfen sie sich fallen lassen, endlich an sich selbst denken. Für solche Frauen beginnt mit den hormonellen Wallungen eine Phase des Perspektivwechsels. Die Zeit des Klimakteriums lädt zu einer inneren Inventur und gegebenenfalls einer Neuorientierung ein. Statt von einem Gefühlschaos überwältigt zu werden, empfinden sich viele Frauen als emotionell empfindsamer, zugänglicher und berührbarer. Moderatorin und Sängerin Lena Kramer nimmt’s mit Humor. Sie nennt die Wechseljahre ihren „inneren Sommer“ und träumt von einer implantierten Klimaanlage.</p>

  <h2 class="section-title title-learn">Wenn Sie erfahren möchten,</h2>
  <ul class="points learn-a">
    <li>wie sich Ihr Körper in den<br>Wechseljahren verändert,</li>
    <li>welche Beschwerden dadurch<br>verursacht werden können</li>
  </ul>
  <ul class="points learn-b">
    <li>was Sie aktiv zur Linderung und<br>Vorbeugung beitragen können,</li>
    <li>wie Sie Ihre eigene Balance<br>und Heilung finden</li>
  </ul>

  <h2 class="section-title title-know">Wollen Sie wissen:</h2>
  <ul class="points know">
    <li>Was mit Ihnen passiert und wie Sie diese neue Lebensphase<br>auf natürliche Weise bewältigen und annehmen können</li>
    <li>Worum es wirklich geht in diesen Jahren</li>
    <li>Wie Sie mutig und lustvoll durch die Wechseljahre kommen</li>
    <li>Mehr wissen über Östrogene, Progesterone und Testosterone</li>
    <li>Dieser Tag macht Mut zum Aufbruch und Neugier auf diese<br>neue Lebensphase. Sie erleben, wie es sein wird, Altes<br>loszulassen, den Blick nach vorn zu richten und wichtige<br>Weichen für Ihren weiteren Lebensweg zu stellen.</li>
  </ul>

  <div class="info-circle">
    <p class="time">VON <b>9.00 – 15.00</b> UHR</p>
    <p class="place"><span class="thin">ORT:</span> BILDUNGSHAUS ST.<br>ALDER, 3930 RIEDMATT</p>
    <p class="price">CHF <b>139.</b><sup>00</sup></p>
    <p class="note">Kosten Seminar inkl. Getränke, Obst,<br>Z’Nüni und 4 Gang Mittags Menu:</p>
  </div>
  <div class="brand-circle">Liebe wachsen</div>

  <section class="band">
    <p>Dieser Tag macht Mut zum Aufbruch und Neugier auf diese neue Lebensphase. Sie erleben, wie es sein wird, Altes loszulassen, den Blick nach vorn zu richten und wichtige Weichen für Ihren weiteren Lebensweg zu stellen.</p>
  </section>
  <div class="portrait" role="img" aria-label="Porträtfoto der Seminarleiterin"></div>

  <footer class="signup">
    <h3>Anmeldung unter:</h3>
    <p class="accent">www.lebensmitte-kurs.ch / info@liebe-wachsen.ch / 079 / 41 26 518</p>
    <p><span class="accent">Mara Lindqvist</span>, Dipl. Wechseljahresberaterin, Sexualtherapeutin und Mentaltrainerin</p>
    <p class="accent">www.Liebe-wachsen.ch</p>
  </footer>
</main>
</body>
</html>
```